Nine Lanterns Quill House Book Cover for: "Growing Older Wisely"

We are a publishing company who plans to launch the book, Growing Older Wisely, A Handy Compact Manual for Legal, Financial and Emotional Health in late 2018. We desire a book cover that creates interest, looks professional and can draw readers to open and purchase this book. Growing Older Wisely is an invaluable, self-help book which provides Generation X, Baby Boomers and their families with the following information: steps to obtain valid, reliable wills and trusts, identify and pay for health care, address end of life care and manage grief. (Please see the attached book description for more information about the book contents). The cover needs to have a "wellness", health and healing emphasis but it should not be morbid. Instead, the cover should have an uplifting, inviting and engaging feeling.

The designer should use Photoshop to develop the 5 x 7 cover. Please design the front, back cover and spine using the attached suggested layout as a guide. Use colors that complement the background colors in the author's photo and the logo for the front and back colors. Feel free to change the colors of the black rectangles on the front of the book. We are looking for a design to be added using the suggested layouts but we are open to modifications of the layout provided that all the content in the attachments are used. Below are the specifications needed for the cover:

-Use Photoshop
-Develop a front and back cover for a 5 x 7 format book
-Include the book title, subtitle and author name on the front cover as noted on the front cover attachment
-Include a book title and author names on the spine of the cover
-Use full bleed background if appropriate
-Color correct and resize images as necessary
-Insert logo and publisher’s imprint on spine and back cover as noted in attachments

For designers who are successful with this contest, we will primarily consider you for future projects.

Thanks!

Target Market(s)

Generation X, Baby Boomers and their families

Industry/Entity Type

Book Publisher

Font styles to use
Sans Serif

Colors

Designer to choose colors to be used in the design.

Requirements
Must have
• The designer should use Photoshop to develop the 5 x 7 cover. Please design the front, back cover and spine using the attached suggested layout as a guide. Use colors that complement the background colors in the author's photo and the logo for the front and back colors. Feel free to change the colors of the black rectangles on the front of the book. We are looking for a design to be added using the suggested layouts but we are open to modifications of the layout provided that all the content in the attachments are used. Below are the specifications needed for the cover:
• -Use Photoshop
• -Develop a front and back cover for a 5 x 7 format book
• -Include the book title, subtitle and author name on the front cover as noted on the front cover attachment
• -Include a book title and author names on the spine of the cover
• -Use full bleed background if appropriate
• -Color correct and resize images as necessary
• -Insert logo and publisher’s imprint on spine and back cover as noted in attachments
Nice to have
• N/A
Should not have
• The design should not specifically duplicate the layout samples or include pictures of persons on the cover. We have provided those as a guide; we are looking for innovation and professionalism.

```html
<!DOCTYPE html>
<html lang="en">
<head>
<meta charset="utf-8">
<title>Growing Older Wisely — Book Cover</title>
<link href="https://fonts.googleapis.com/css2?family=Antonio:wght@100;300&family=Archivo+Narrow:ital,wght@0,400;0,700;1,400&family=Fira+Sans+Condensed:wght@600&family=Montserrat:wght@700&display=swap" rel="stylesheet">
<style>
  :root {
    --title-red: #d0101f;
    --spine-red: #c8101e;
    --spine-gold: #fde27a;
    --band-cream: #fde49a;
    --ink: #1d1d1d;
    --leaf-red: #e8323c;
    --leaf-orange: #f78a1d;
    --leaf-yellow: #fcc42a;
    --frame: #555;
  }
  * { box-sizing: border-box; margin: 0; padding: 0; }
  html, body { width: 1200px; height: 1200px; overflow: hidden; background: #fff; }
  .canvas { position: relative; width: 1200px; height: 1200px; background: #fff; }

  .cover {
    position: absolute; left: 65px; top: 271px; width: 1069px; height: 695px;
    border: 1px solid var(--frame); overflow: hidden; background: #fff;
  }

  /* ---------- back cover ---------- */
  .back { position: absolute; left: 0; top: 0; width: 497px; height: 695px; background: #fff; }
  .back__leaves {
    position: absolute; left: 0; top: 0; width: 130px; height: 695px;
    background:
      radial-gradient(ellipse 70px 60px at 60px 60px, var(--leaf-red), transparent 70%),
      radial-gradient(ellipse 60px 70px at 40px 230px, var(--leaf-red), transparent 70%),
      radial-gradient(ellipse 70px 80px at 50px 420px, var(--leaf-orange), transparent 70%),
      radial-gradient(ellipse 70px 70px at 70px 600px, var(--leaf-orange), transparent 70%),
      linear-gradient(90deg, rgba(247,138,29,.55), rgba(252,196,42,.15) 75%, transparent);
  }
  .back__title {
    position: absolute; left: 105px; top: 32px; width: 390px; text-align: center; white-space: nowrap;
    font-family: "Montserrat", sans-serif; font-weight: 700; font-size: 22px; line-height: 28px; color: var(--ink);
  }
  .back__subtitle {
    position: absolute; left: 120px; top: 60px; width: 360px; text-align: center;
    font-family: "Archivo Narrow", sans-serif; font-style: italic; font-size: 13px; line-height: 16px; color: var(--ink);
  }
  .back__copy {
    position: absolute; left: 124px; top: 100px; width: 350px;
    font-family: "Archivo Narrow", sans-serif; font-size: 10.4px; line-height: 15.6px; color: var(--ink);
  }
  .back__copy p { margin-bottom: 6px; }
  .author-photo {
    position: absolute; left: 37px; top: 330px; width: 123px; height: 166px;
    background: linear-gradient(160deg, #8c9a86, #5d6d63 55%, #2f3444);
  }
  .back__bio {
    position: absolute; left: 169px; top: 326px; width: 305px;
    font-family: "Archivo Narrow", sans-serif; font-size: 10.4px; line-height: 15.6px; color: var(--ink);
  }
  .back__bio b { font-weight: 700; }
  .back__web { position: absolute; left: 169px; top: 455px; font-family: "Archivo Narrow", sans-serif; font-size: 10.4px; color: var(--ink); }
  .back__isbn, .back__imprint {
    position: absolute; left: 124px; font-family: "Archivo Narrow", sans-serif; font-size: 10.4px; line-height: 16px; color: var(--ink);
  }
  .back__isbn { top: 508px; }
  .back__imprint { top: 563px; }
  .back__code-box { position: absolute; left: 286px; top: 559px; width: 174px; height: 99px; border: 1px solid #ccc; background: #fff; }
  .publisher-mark {
    position: absolute; left: 38px; top: 640px; display: flex; align-items: center; gap: 6px;
    font-family: "Archivo Narrow", sans-serif; font-weight: 700; font-size: 11.5px; color: var(--ink);
  }
  .publisher-mark__square { width: 14px; height: 14px; background: #1f2a6b; }

  /* ---------- spine ---------- */
  .spine { position: absolute; left: 497px; top: 0; width: 75px; height: 695px; background: var(--spine-red); }
  .spine__titles {
    position: absolute; left: 75px; top: 38px; transform-origin: 0 0; transform: rotate(90deg);
    width: 400px; color: var(--spine-gold);
  }
  .spine__title { font-family: "Antonio", sans-serif; font-weight: 100; font-size: 30px; letter-spacing: 1px; line-height: 36px; padding-left: 8px; white-space: nowrap; }
  .spine__subtitle { font-family: "Archivo Narrow", sans-serif; font-size: 12.5px; line-height: 18px; padding-left: 8px; white-space: nowrap; }
  .spine__authors {
    position: absolute; left: 0; top: 460px; width: 75px; text-align: center; color: var(--spine-gold);
    font-family: "Antonio", sans-serif; font-weight: 100; line-height: .95;
  }
  .spine__authors .name { font-size: 34px; display: block; }
  .spine__authors .with { font-size: 13px; display: block; margin: 3px 0; }
  .spine__publisher {
    position: absolute; left: 7px; top: 640px; display: flex; align-items: center; gap: 3px;
    font-family: "Archivo Narrow", sans-serif; font-size: 5px; color: var(--spine-gold);
  }
  .spine__publisher span:first-child { width: 9px; height: 9px; background: #1f2a6b; }

  /* ---------- front cover ---------- */
  .front { position: absolute; left: 572px; top: 0; width: 497px; height: 695px; background: #fff; }
  .front__leaves-left, .front__leaves-right { position: absolute; top: 0; height: 695px; }
  .front__leaves-left {
    left: 0; width: 175px;
    background:
      radial-gradient(ellipse 80px 90px at 60px 120px, var(--leaf-yellow), transparent 70%),
      radial-gradient(ellipse 90px 80px at 110px 390px, var(--leaf-red), transparent 70%),
      radial-gradient(ellipse 90px 90px at 70px 560px, var(--leaf-orange), transparent 70%),
      linear-gradient(90deg, var(--leaf-orange), rgba(252,196,42,.7) 65%, transparent);
  }
  .front__leaves-right {
    right: 0; width: 150px;
    background:
      radial-gradient(ellipse 80px 80px at 80px 120px, var(--leaf-red), transparent 70%),
      radial-gradient(ellipse 80px 90px at 100px 290px, var(--leaf-red), transparent 70%),
      radial-gradient(ellipse 80px 90px at 70px 470px, var(--leaf-yellow), transparent 70%),
      linear-gradient(270deg, var(--leaf-orange), rgba(252,196,42,.65) 65%, transparent);
  }
  .front__quote-band {
    position: absolute; left: 140px; top: 16px; width: 250px; height: 70px; background: var(--band-cream);
    text-align: center; padding-top: 14px;
  }
  .front__quote { font-family: "Fira Sans Condensed", sans-serif; font-weight: 600; font-size: 24px; color: var(--title-red); line-height: 26px; }
  .front__source { font-family: "Archivo Narrow", sans-serif; font-style: italic; font-size: 14px; color: var(--title-red); }
  .front__title {
    position: absolute; left: 100px; top: 100px; width: 340px; text-align: center;
    font-family: "Antonio", sans-serif; font-weight: 100; color: var(--title-red);
    font-size: 112px; line-height: 104px;
  }
  .front__title span { display: block; transform: scaleX(.62); transform-origin: 50% 50%; }
  .front__subtitle {
    position: absolute; left: 120px; top: 425px; width: 300px; text-align: center;
    font-family: "Archivo Narrow", sans-serif; font-style: italic; font-size: 26px; line-height: 32px; color: var(--ink);
  }
  .front__author-band {
    position: absolute; left: 110px; top: 605px; width: 387px; height: 76px; background: var(--band-cream);
    text-align: center; padding-top: 10px;
    font-family: "Fira Sans Condensed", sans-serif; font-weight: 600; font-size: 22px; line-height: 26px; color: var(--ink);
  }
</style>
</head>
<body>
<div class="canvas">
  <div class="cover">

    <section class="back">
      <div class="back__leaves" role="img" aria-label="Watercolour autumn leaves in red, orange and yellow along the edge"></div>
      <h2 class="back__title">GROWING OLDER WISELY</h2>
      <p class="back__subtitle">A Handy Compact Manual<br>for Legal, Financial and Emotional Health</p>
      <div class="back__copy">
        <p>Death and taxes may be inevitable, but they both require a lot of preparation. Fifty percent of America’s seventy-four million baby boomers have parents eighty or older, and nearly half of those boomers haven’t discussed end-of-life issues with their loved ones.</p>
        <p>In <i>Growing Older Wisely</i>, the authors present a detailed, step-by-step guide on how to deal with aging. They tackle issues such as wills and trusts, estate planning, senior housing, caregiving, hospice care, and death and bereavement. Their approach is lighthearted but thorough, and they provide a sorely needed examination of all the details involved in growing old in America.</p>
        <p>Nadine R. Vale is a social services administrator, and Contributor Owen T. Brask is an attorney. They have combined their skills and knowledge to give readers a practical understanding of the issues involved in caring for an elderly family member.</p>
      </div>
      <div class="author-photo" role="img" aria-label="Portrait photograph of the author"></div>
      <p class="back__bio"><b>Nadine R. Vale</b> holds an advanced degree in Public Administration from Harborview State University and is currently an Administrator at the Westmere Department of Community Services. Collaborator Owen T. Brask is an attorney who has practiced for thirty-five years in the areas of family law, wills, trusts, and estate planning. In <i>Growing Older Wisely</i>, the two have pooled their expertise to provide an invaluable guide to all the issues involved in caring for a loved one at the end of his or her life.</p>
      <p class="back__web">www.nadinevalewrites.com</p>
      <p class="back__isbn">ISBN: 978-0-000-41827-3 (paperback)<br>ISBN: 978-0-000-52964-8 (ebook)</p>
      <p class="back__imprint">NINE LANTERNS QUILL HOUSE<br>An Imprint of Nine Lanterns Quill</p>
      <div class="back__code-box"></div>
      <div class="publisher-mark"><span class="publisher-mark__square"></span><span>Nine Lanterns Quill</span></div>
    </section>

    <section class="spine">
      <div class="spine__titles">
        <div class="spine__title">GROWING OLDER WISELY</div>
        <div class="spine__subtitle">A Handy Compact Manual for Legal, Financial and Emotional Health</div>
      </div>
      <div class="spine__authors">
        <span class="name">VALE</span>
        <span class="with">WITH</span>
        <span class="name">BRASK</span>
      </div>
      <div class="spine__publisher"><span></span><span>Nine Lanterns Quill</span></div>
    </section>

    <section class="front">
      <div class="front__leaves-left" role="img" aria-label="Watercolour autumn leaves in orange, red and yellow"></div>
      <div class="front__leaves-right" role="img" aria-label="Watercolour autumn leaves in red, orange and yellow"></div>
      <div class="front__quote-band">
        <p class="front__quote">"Indispensable!"</p>
        <p class="front__source">– The Riverbend Ledger</p>
      </div>
      <h1 class="front__title"><span>GROWING</span><span>OLDER</span><span>WISELY</span></h1>
      <p class="front__subtitle">A Handy<br>Compact Manual<br>for Legal, Financial<br>and<br>Emotional Health</p>
      <div class="front__author-band">NADINE R. VALE, M.P.A.<br>with OWEN T. BRASK, ESQ.</div>
    </section>

  </div>
</div>
</body>
</html>
```